Business card design to promote website

SaferStreetsNow.org is a website designed for parents and other community members seeking information and other resources in the tri-county area (San Luis Obispo, Santa Barbara & Ventura Counties) about gang reduction, intervention and prevention. We are looking for a bold,eye-catching, full-color card one with a full graphic background, possibly depicting a "street" scene with police, or gang members, or dead body outline or other crime scene image. One side in English and other side in Spanish.

Target Market(s)

Parents and other community members concerned about gangs, violence, and youth & community safety

Industry/Entity Type

Business

Contact Information for Business Card

SaferStreetsNow.org
Serving San Luis Obispo, Santa Barbara & Ventura Counties

Requirements
Must have
• Design must have bold full graphic design front, and include web address. (Attached images are just inspirational; we do not own the rights to these images.) Please visit the website www.SaferStreetsNow.org to gain an understanding of the look and feel.

```html
<!DOCTYPE html>
<html lang="en">
<head>
<meta charset="utf-8">
<title>SaferStreetsNow.org – Business Cards</title>
<link rel="stylesheet" href="https://fonts.googleapis.com/css2?family=Source+Sans+3:wght@400;600&display=swap">
<style>
  :root {
    --page: #e9e6e2;
    --card-red: #b8252f;
    --card-red-deep: #a01f28;
    --card-black: #0d0d0d;
    --splash-light: #f4f4f4;
    --splash-grey: #c4c4c4;
    --accent-yellow: #e2b21c;
    --silhouette: #141414;
    --text-light: #f5ecec;
  }
  html, body {
    margin: 0;
    width: 1200px;
    height: 776px;
    overflow: hidden;
    background: var(--page);
    font-family: "Source Sans 3", "Myriad Pro", Arial, sans-serif;
  }
  .sheet {
    width: 1200px;
    height: 776px;
    display: flex;
    align-items: center;
    justify-content: center;
    gap: 40px;
  }
  .card {
    position: relative;
    width: 540px;
    height: 310px;
    overflow: hidden;
    box-shadow: 0 6px 18px rgba(0,0,0,0.25);
  }
  .card-art {
    position: absolute;
    inset: 0;
    width: 100%;
    height: 100%;
  }
  .card-text {
    position: absolute;
    left: 150px;
    right: 30px;
    bottom: 22px;
    text-align: center;
    color: var(--text-light);
  }
  .web-address {
    margin: 0;
    font-size: 24px;
    font-weight: 600;
    line-height: 1.1;
  }
  .service-area {
    margin: 7px 0 0;
    font-size: 11.5px;
    font-weight: 400;
    white-space: nowrap;
  }
</style>
</head>
<body>
<main class="sheet">

  <section class="card card--spanish" lang="es">
    <svg class="card-art" viewBox="0 0 540 310">
      <defs>
        <linearGradient id="splashEs" x1="0" y1="0" x2="1" y2="1">
          <stop offset="0" stop-color="var(--splash-light)"/>
          <stop offset="1" stop-color="var(--splash-grey)"/>
        </linearGradient>
      </defs>
      <rect class="field-red" width="540" height="310" fill="var(--card-red)"/>
      <polygon class="band-black" points="0,0 540,0 540,118 0,150" fill="var(--card-black)"/>
      <polygon class="accent-stripe" points="448,40 464,40 420,196 404,196" fill="var(--accent-yellow)"/>
      <polygon class="splash-area" fill="url(#splashEs)" role="img" aria-label="Rough white brush-stroke paint splash"
        points="150,46 170,62 182,30 200,56 214,24 232,50 252,20 268,48 290,28 300,52 322,34 334,60 352,44 360,72
                388,66 372,96 396,104 376,126 398,146 372,160 390,186 360,192 372,214 336,210 320,228 296,214
                270,230 246,214 218,226 196,212 160,222 150,206 110,214 126,196 60,200 104,184 40,180 96,168
                34,160 100,150 56,140 110,132 84,118 126,108 110,88 140,82 128,62"/>
      <rect class="silhouette-area" x="160" y="78" width="150" height="108" rx="6" fill="var(--silhouette)"
            role="img" aria-label="Black handgun silhouette"/>
    </svg>
    <div class="card-text">
      <p class="web-address">www.SaferStreetsNow.org</p>
      <p class="service-area">Sirviendo en las ciudades de: San Luis Obispo, Santa Barbara &amp; Ventura</p>
    </div>
  </section>

  <section class="card card--english" lang="en">
    <svg class="card-art" viewBox="0 0 540 310">
      <defs>
        <linearGradient id="splashEn" x1="0" y1="0" x2="1" y2="1">
          <stop offset="0" stop-color="var(--splash-light)"/>
          <stop offset="1" stop-color="var(--splash-grey)"/>
        </linearGradient>
      </defs>
      <rect class="field-red" width="540" height="310" fill="var(--card-red)"/>
      <polygon class="band-black" points="0,0 540,0 540,118 0,150" fill="var(--card-black)"/>
      <polygon class="accent-stripe" points="448,40 464,40 420,196 404,196" fill="var(--accent-yellow)"/>
      <polygon class="splash-area" fill="url(#splashEn)" role="img" aria-label="Rough white brush-stroke paint splash"
        points="150,46 170,62 182,30 200,56 214,24 232,50 252,20 268,48 290,28 300,52 322,34 334,60 352,44 360,72
                388,66 372,96 396,104 376,126 398,146 372,160 390,186 360,192 372,214 336,210 320,228 296,214
                270,230 246,214 218,226 196,212 160,222 150,206 110,214 126,196 60,200 104,184 40,180 96,168
                34,160 100,150 56,140 110,132 84,118 126,108 110,88 140,82 128,62"/>
      <rect class="silhouette-area" x="160" y="78" width="150" height="108" rx="6" fill="var(--silhouette)"
            role="img" aria-label="Black handgun silhouette"/>
    </svg>
    <div class="card-text">
      <p class="web-address">www.SaferStreetsNow.org</p>
      <p class="service-area">Serving San Luis Obispo, Santa Barbara &amp; Ventura Counties</p>
    </div>
  </section>

</main>
</body>
</html>
```